Willowmere Surgery Brochure Design

Willowmere Surgery (willowmeresurgery.example)

Is a comprehensive breast care center that focuses on caring for women with breast cancer and other breast pathologies. We need a promotional and marketing brochure, in a tri-fold format, to provide information about our office and describe the services that we offer.

Deliverable

* The brochure should be completed by August 24th
* We will need the necessary files to get the brochure printed (.ai, .indd, etc).

Target Market(s)

Primarily patients of age between 30+ and 70+. The brochure will also be placed in doctor's waiting room

Industry/Entity Type

Marketing

Requirements
Must have
• * Make use of the color scheme as the website (http://willowmeresurgery.example, http://willowmeresurgery.example/static/theme-fuchsia.png)
* Incorporate the following graphic elements:
* The company’s logo (provided as an attachment)
* At least one images from the homepage
* Photos of the primary doctor and her staff
* Map to show the office location and phone number
* Enclose a breast cancer self-exam card (http://willowmeresurgery.example/static/shower-card.jpg)
* A portion of the brochure must be detachable and serve as business cards that can be cut off (see attachment).
Nice to have
• Here is an example of a brochure that we like:

http://plakmarket.example/item/flexible-trifold-brochure/731284?WT.ac=search_item&WT.seg_1=search_item&WT.z_author=dembrovi

```html
<!DOCTYPE html>
<html lang="en">
<head>
<meta charset="utf-8">
<title>Willowmere Surgery – Breast Care Brochure</title>
<link rel="stylesheet" href="https://fonts.googleapis.com/css2?family=Gelasio:wght@400;700&family=Pinyon+Script&family=Great+Vibes&display=swap">
<style>
  :root {
    --pink: #f4aecb;
    --maroon: #6e1f30;
    --magenta: #b0336e;
    --ink: #4a2a30;
    --grey: #959595;
    --white: #ffffff;
    --petal-light: #f9e6ee;
    --petal-mid: #f0c4d6;
  }
  * { box-sizing: border-box; margin: 0; padding: 0; }
  html, body { width: 1080px; height: 1200px; overflow: hidden; background: var(--white); }
  .brochure { position: relative; width: 1080px; height: 1200px; font-family: "Gelasio", Georgia, serif; color: var(--ink); }

  .header { position: absolute; left: 0; top: 0; width: 1080px; height: 140px; }
  .section-title { position: absolute; left: 90px; top: 44px; font-family: "Great Vibes", cursive; font-size: 44px; color: var(--magenta); font-weight: 400; }
  .flower-art { position: absolute; left: 568px; top: 0; width: 226px; height: 168px; border-radius: 0 0 24px 24px;
    background: linear-gradient(160deg, var(--petal-light) 0%, var(--petal-mid) 100%); z-index: 3; }
  .brand-name { position: absolute; left: 806px; top: 58px; font-family: "Gelasio", Georgia, serif; font-size: 27px; color: var(--magenta); }

  .panel-band { position: absolute; left: 0; top: 140px; width: 1080px; height: 623px; }

  .col { position: absolute; font-size: 13px; line-height: 15.6px; }
  .col p { margin-bottom: 18px; }
  .col-info { left: 29px; top: 172px; width: 304px; }
  .col-info .web { text-align: center; font-weight: 700; }
  .col-info .gap { margin-top: 27px; }
  .col-find { left: 389px; top: 172px; width: 310px; font-size: 14px; line-height: 17px; }
  .col-find h2 { font-size: 15.5px; font-weight: 700; margin-bottom: 18px; }
  .col-find .address { margin-top: 34px; }

  .map-area { position: absolute; left: 381px; top: 393px; width: 319px; height: 212px; background: var(--white); padding: 6px; }
  .map-area div { width: 100%; height: 100%; background: linear-gradient(155deg, #e4e0d9, #ece9e3 60%, #f0eeea); }

  .photo-frame { position: absolute; left: 751px; top: 175px; width: 305px; height: 396px; border: 5px solid var(--maroon); border-radius: 0 34px 0 34px;
    background: linear-gradient(180deg, #f3dce4 0%, #d79aab 50%, #8b3448 100%); overflow: hidden; }
  .photo-frame .tagline { position: absolute; left: 14px; top: 14px; font-family: "Pinyon Script", cursive; font-size: 21px; color: var(--maroon); }

  .doctor-contact { position: absolute; left: 756px; top: 664px; width: 280px; text-align: center; font-size: 14.2px; line-height: 18px; font-style: normal; }
  .doctor-contact strong { font-size: 14.8px; }

  .cards { position: absolute; left: 0; top: 763px; width: 358px; height: 437px; background: var(--white); }
  .card { position: absolute; left: 0; width: 358px; height: 218px; transform: rotate(180deg); text-align: center; color: var(--ink); }
  .card-1 { top: 0; }
  .card-2 { top: 220px; }
  .card .brand { font-family: "Gelasio", Georgia, serif; font-size: 30px; color: var(--magenta); margin-top: 42px; }
  .card .details { margin-top: 38px; font-size: 13px; line-height: 19px; }
  .card .details strong { font-size: 13.5px; }
  .cut-line { position: absolute; left: 0; top: 978px; width: 358px; border-top: 1px dotted #777; }

  .back-blank { position: absolute; left: 358px; top: 763px; width: 722px; height: 437px; background: var(--grey); }
</style>
</head>
<body>
<div class="brochure">
  <svg class="panel-band" viewBox="0 0 1080 623" aria-hidden="true">
    <path d="M0 4 H960 Q1080 4 1080 90 V623 H0 Z" fill="var(--pink)"/>
    <path d="M0 4 H960 Q1080 4 1080 90" fill="none" stroke="var(--maroon)" stroke-width="6"/>
  </svg>

  <header class="header">
    <h1 class="section-title">Breast Care</h1>
    <div class="brand-name">Willowmere Surgery</div>
  </header>
  <div class="flower-art" role="img" aria-label="Decorative image of pink and white lotus flowers"></div>

  <section class="col col-info">
    <p>To learn more information about Dr. Halloran, the services we offer, important clinical information and all that you need to know concerning insurance and payment, please visit our website:</p>
    <p class="web">www.willowmeresurgery.example</p>
    <p>There, you can download any forms that will need to be printed and completed prior to your visit.</p>
    <p class="gap">There is also a great question-and-answer section which covers many common queries.</p>
    <p class="gap">Additionally, you can email Dr. Halloran directly at <strong>willowmere.surgery@example.com</strong> it's easy and confidential.</p>
    <p class="gap">To schedule an appointment, please call us on <strong>(555) 014-2052.</strong></p>
    <p class="gap">We look forward to hearing from you soon and participating in your medical care.</p>
  </section>

  <section class="col col-find">
    <h2>How to Find Us</h2>
    <p>We are located at the Breast Center inside the Marlowe Ashby Cancer Center</p>
    <p>On the campus of Brookhaven Hospital</p>
    <p class="address">4410 Linden Crest Dr,<br>Suite 100 Fairbrook, IL 60000<br>Phone: (555) 014-2052<br>Fax: (555) 014-6683</p>
  </section>

  <div class="map-area"><div role="img" aria-label="Street map showing the cancer center location near the hospital"></div></div>

  <div class="photo-frame">
    <div role="img" aria-label="Photo of a smiling woman embracing herself, with a decorative vine ornament" style="position:absolute;inset:0;"></div>
    <span class="tagline">Comprehensive Breast Care</span>
  </div>

  <address class="doctor-contact">
    <strong>Dr. Halloran</strong><br>
    Phone: (555) 014-2052<br>
    Email: willowmere.surgery@example.com<br>
    www.willowmeresurgery.example
  </address>

  <div class="cards">
    <div class="card card-1">
      <div class="brand">Willowmere Surgery</div>
      <div class="details"><strong>Dr. Halloran</strong><br>Phone: (555) 014-2052<br>Email: willowmere.surgery@example.com<br>www.willowmeresurgery.example</div>
    </div>
    <div class="card card-2">
      <div class="brand">Willowmere Surgery</div>
      <div class="details"><strong>Dr. Halloran</strong><br>Phone: (555) 014-2052<br>Email: willowmere.surgery@example.com<br>www.willowmeresurgery.example</div>
    </div>
  </div>
  <div class="cut-line"></div>
  <div class="back-blank"></div>
</div>
</body>
</html>
```